Steadfast MD - Sleep Medicine Specialist - Business Cards

We are a new medical practice called Steadfast MD. We are sleep medicine specialists and we will be conducting sleep studies on patients with sleep related ailments. We want the business card to be bold, professional, and clean with the logo as the stand out visual piece. We dont like wild flashy designs. We want our design to be bold and classic while at the same time conveying who we are and what we do. We are reliable, professional, and the best in the business.

Industry/Entity Type

Health Care

Contact Information for Business Card

- Clean
- Bold
- Classic
- not cluttered

Requirements
Must have
• logo, website, phone number
Nice to have
• several options to choose from
Should not have
• flashy imaged - reflective print - images of people sleeping

```html
<!DOCTYPE html>
<html lang="en">
<head>
<meta charset="utf-8">
<title>Steadfast MD – Business Cards</title>
<link rel="stylesheet" href="https://fonts.googleapis.com/css2?family=Oswald:wght@500&family=Work+Sans:wght@400;700&display=swap">
<style>
  :root {
    --bg: #161616;
    --card: #262626;
    --card-edge: #2e2e2e;
    --red: #e3141b;
    --white: #f2f2f2;
    --silver: #8a8a8a;
  }
  * { margin: 0; padding: 0; box-sizing: border-box; }
  html, body { width: 1200px; height: 900px; overflow: hidden; }
  body {
    background: var(--bg);
    font-family: "Work Sans", Arial, sans-serif;
    display: flex;
    flex-direction: column;
    align-items: center;
    justify-content: center;
    gap: 36px;
  }
  .card {
    width: 700px;
    height: 400px;
    background: var(--card);
    border: 1px solid var(--card-edge);
    position: relative;
  }
  .card-front {
    display: flex;
    align-items: center;
    justify-content: center;
  }
  .brand {
    display: flex;
    align-items: center;
    gap: 16px;
    font-family: "Work Sans", Arial, sans-serif;
    font-weight: 700;
    letter-spacing: -0.5px;
  }
  .brand-mark {
    border-radius: 50%;
    border: 3px solid currentColor;
    flex: none;
  }
  .card-front .brand { color: var(--silver); font-size: 48px; }
  .card-front .brand-mark { width: 72px; height: 72px; }
  .card-back .brand {
    position: absolute;
    top: 52px;
    left: 50%;
    transform: translateX(-50%);
    color: var(--white);
    font-size: 40px;
    white-space: nowrap;
  }
  .card-back .brand-mark { width: 62px; height: 62px; color: var(--red); }
  .details {
    position: absolute;
    top: 178px;
    left: 0;
    right: 0;
    display: flex;
    justify-content: center;
    align-items: center;
  }
  .person { text-align: right; padding-right: 28px; }
  .person-name {
    font-family: "Oswald", "Arial Narrow", sans-serif;
    font-weight: 500;
    font-size: 40px;
    color: var(--red);
    line-height: 1.05;
    letter-spacing: 0.5px;
  }
  .person-role { color: var(--white); font-size: 18px; letter-spacing: 1px; }
  .divider { width: 2px; height: 74px; background: var(--red); }
  .contact-list { list-style: none; padding-left: 28px; }
  .contact-list li {
    display: flex;
    align-items: center;
    gap: 10px;
    color: var(--white);
    font-size: 18px;
    letter-spacing: 0.8px;
    line-height: 1.4;
  }
  .contact-list svg { width: 14px; height: 14px; flex: none; }
  .address {
    position: absolute;
    bottom: 58px;
    left: 0;
    right: 0;
    text-align: center;
    color: var(--white);
    font-size: 19px;
    letter-spacing: 1.2px;
  }
</style>
</head>
<body>
  <section class="card card-front">
    <div class="brand"><span class="brand-mark"></span>Steadfast MD</div>
  </section>

  <section class="card card-back">
    <div class="brand"><span class="brand-mark"></span>Steadfast MD</div>
    <div class="details">
      <div class="person">
        <div class="person-name">DANIEL CARTER</div>
        <div class="person-role">Founder</div>
      </div>
      <div class="divider"></div>
      <ul class="contact-list">
        <li>
          <svg viewBox="0 0 24 24" fill="none" stroke="#e3141b" stroke-width="2.4" stroke-linecap="round" stroke-linejoin="round"><path d="M5 3h4l2 5-3 2a11 11 0 0 0 6 6l2-3 5 2v4a2 2 0 0 1-2 2A17 17 0 0 1 3 5a2 2 0 0 1 2-2z"/></svg>
          555 014-2270
        </li>
        <li>
          <svg viewBox="0 0 24 24" fill="none" stroke="#e3141b" stroke-width="2.4" stroke-linejoin="round"><rect x="3" y="5" width="18" height="14"/><path d="M3 6l9 7 9-7"/></svg>
          info@steadfastmd.com
        </li>
        <li>
          <svg viewBox="0 0 24 24" fill="none" stroke="#e3141b" stroke-width="2.2"><circle cx="12" cy="12" r="9"/><path d="M3 12h18M12 3c3 3 3 15 0 18M12 3c-3 3-3 15 0 18"/></svg>
          www.steadfastmd.com
        </li>
      </ul>
    </div>
    <p class="address">418 Harlow Avenue Riverton, MO 63201</p>
  </section>
</body>
</html>
```